Real estate investment and development Business Visiting cards

Visiting cards for our company
We develop flats and rent them out, Now we planning to offer investors new investment opportunities in the UK Real estate sector. we used to have a design for our visiting card but we do not like it anymore. we want to have different designs keeping the same colors with our websites and company. I will attach our previous Visiting card model.

Target Market(s)

Private Investors, Banks,

Industry/Entity Type

Real Estate Development

Contact Information for Business Card

RVKT Holdings
Tomas Ferrell Director
Info to be included
3-Info

Tel
(+44 )7481 203917

Email

tomas@rvkt.co.uk

info@rvkt.co.uk

Address

17 Gorsefield Lane, Stratford, London, E15 4RW

Website

rvktholdings.co.uk

Font styles to use
Serif

Colors
f78f20
fef5ee

Requirements
Must have
• The colours of the company and the Logo
Nice to have
• Modern idea and icons on the info
A code bar that directs to the website
Should not have
• a lot from the orange colour

```html
<!DOCTYPE html>
<html lang="en">
<head>
<meta charset="utf-8">
<title>RVKT Holdings – Business Cards</title>
<link rel="stylesheet" href="https://fonts.googleapis.com/css2?family=Libre+Baskerville&family=Lato:wght@400&display=swap">
<style>
  :root {
    --backdrop: #2b2b2b;
    --card: #0a0a0a;
    --orange: #f78f20;
    --white: #f4f4f4;
    --grey: #c9c9c9;
    --silver: #a9a9a9;
    --serif: "Libre Baskerville", "Times New Roman", serif;
    --sans: "Lato", Arial, sans-serif;
  }
  * { margin: 0; padding: 0; box-sizing: border-box; }
  html, body { width: 1200px; height: 900px; overflow: hidden; }
  body {
    background: var(--backdrop);
    display: flex;
    align-items: center;
    justify-content: center;
    gap: 40px;
  }
  .card {
    position: relative;
    width: 540px;
    height: 330px;
    background: var(--card);
    box-shadow: 0 14px 40px rgba(0,0,0,.55);
  }

  /* Front */
  .brand {
    position: absolute;
    left: 42px;
    top: 48px;
    display: flex;
    align-items: center;
    gap: 22px;
  }
  .brand-square {
    width: 78px;
    height: 78px;
    background: var(--orange);
  }
  .brand-name {
    font-family: var(--serif);
    font-size: 62px;
    color: var(--white);
    letter-spacing: 1px;
    line-height: 1;
  }
  .details {
    position: absolute;
    left: 142px;
    top: 142px;
  }
  .person {
    display: flex;
    align-items: baseline;
    gap: 12px;
  }
  .person-name {
    font-family: var(--serif);
    font-size: 21px;
    color: var(--orange);
    text-transform: uppercase;
    letter-spacing: 1px;
  }
  .person-role {
    font-family: var(--sans);
    font-size: 14px;
    color: var(--grey);
  }
  .rule {
    width: 72px;
    height: 1px;
    background: var(--orange);
    margin: 6px 0 8px;
  }
  .contact-list { list-style: none; }
  .contact-list li {
    display: flex;
    align-items: center;
    gap: 9px;
    font-family: var(--sans);
    font-size: 13.5px;
    color: var(--grey);
    line-height: 20px;
  }
  .contact-list svg { width: 14px; height: 14px; flex: none; fill: var(--orange); }
  .accent { color: var(--orange); }
  .office {
    display: flex;
    gap: 9px;
    font-family: var(--sans);
    font-size: 14px;
    color: var(--grey);
    line-height: 19px;
  }
  .office svg { width: 14px; height: 16px; flex: none; fill: var(--orange); margin-top: 2px; }
  .office-name { color: var(--orange); }

  /* Back */
  .back-brand {
    position: absolute;
    left: 0; right: 0;
    top: 112px;
    display: flex;
    align-items: center;
    justify-content: center;
    gap: 20px;
  }
  .back-square {
    width: 70px;
    height: 70px;
    border: 9px solid #6b6b6b;
    background: #1a1a1a;
  }
  .back-name {
    font-family: var(--serif);
    font-size: 60px;
    color: var(--silver);
    letter-spacing: 1px;
    line-height: 1;
  }
  .back-url {
    position: absolute;
    left: 0; right: 0;
    top: 212px;
    text-align: center;
    font-family: var(--serif);
    font-size: 13px;
    letter-spacing: 4px;
    color: #8a8a8a;
  }
</style>
</head>
<body>

<section class="card card-front">
  <div class="brand">
    <div class="brand-square"></div>
    <div class="brand-name">RVKT</div>
  </div>

  <div class="details">
    <div class="person">
      <span class="person-name">Tomas Ferrell</span>
      <span class="person-role">Director</span>
    </div>
    <div class="rule"></div>
    <ul class="contact-list">
      <li>
        <svg viewBox="0 0 24 24" aria-hidden="true"><path d="M6.6 10.8a15.1 15.1 0 0 0 6.6 6.6l2.2-2.2a1 1 0 0 1 1-.25 11.4 11.4 0 0 0 3.6.57 1 1 0 0 1 1 1V20a1 1 0 0 1-1 1A17 17 0 0 1 3 4a1 1 0 0 1 1-1h3.5a1 1 0 0 1 1 1c0 1.25.2 2.45.57 3.57a1 1 0 0 1-.25 1z"/></svg>
        (+44 )7481 203917
      </li>
      <li>
        <svg viewBox="0 0 24 24" aria-hidden="true"><path d="M2 5h20v14H2zm2 2v.4l8 5.2 8-5.2V7zm0 2.8V17h16V9.8l-8 5.2z"/></svg>
        tomas@rvkt.co.uk | info@rvkt.co.uk
      </li>
      <li>
        <svg viewBox="0 0 24 24" aria-hidden="true"><path d="M12 2a10 10 0 1 0 0 20 10 10 0 0 0 0-20zm6.9 6h-3a15 15 0 0 0-1.3-3.9A8 8 0 0 1 18.9 8zM12 4a13 13 0 0 1 1.9 4h-3.8A13 13 0 0 1 12 4zM4.3 14a8 8 0 0 1 0-4h3.4a16 16 0 0 0 0 4zm.8 2h3a15 15 0 0 0 1.3 3.9A8 8 0 0 1 5.1 16zm3-8h-3a8 8 0 0 1 4.3-3.9A15 15 0 0 0 8.1 8zM12 20a13 13 0 0 1-1.9-4h3.8A13 13 0 0 1 12 20zm2.3-6H9.7a14 14 0 0 1 0-4h4.6a14 14 0 0 1 0 4zm.3 5.9a15 15 0 0 0 1.3-3.9h3a8 8 0 0 1-4.3 3.9zm1.7-5.9a16 16 0 0 0 0-4h3.4a8 8 0 0 1 0 4z"/></svg>
        <span>www.<span class="accent">rvktholdings</span>.co.uk</span>
      </li>
    </ul>
    <div class="rule"></div>
    <div class="office">
      <svg viewBox="0 0 24 28" aria-hidden="true"><path d="M12 0a9 9 0 0 0-9 9c0 6.8 9 19 9 19s9-12.2 9-19a9 9 0 0 0-9-9zm0 12.5A3.5 3.5 0 1 1 12 5.5a3.5 3.5 0 0 1 0 7z"/></svg>
      <address style="font-style:normal">
        <span class="office-name">RVKT Holdings</span><br>
        17 Gorsefield Lane<br>
        Stratford, London, E15 4RW
      </address>
    </div>
  </div>
</section>

<section class="card card-back">
  <div class="back-brand">
    <div class="back-square"></div>
    <div class="back-name">RVKT</div>
  </div>
  <div class="back-url">www.rvktholdings.co.uk</div>
</section>

</body>
</html>
```